Never Stay Meek needs a book cover design

I need a book cover design for the following title:
Never Stay Meek-Grow a Bold Captain
Family methods from Cradle to Silver Years
by Dr. Walter P. Ondrak
I am interviewing a number of strong Canadian Leaders-specifically with regard to their experience of being parented. The book is a reaction today of parents having no backbone, no will nor ability to discipline their children. Many parents want to make a change but don't know how to.
Updates
Title should be "Never Stay Meek-Grow a Bold Captain" the rest is correct Added Wednesday, November 11, 2015
Here is an example of what we would need on the back cover in text only.
What does it take to raise a strong leader? Psychologist Dr. Walter P. Ondrak provides you with 6 must do strategies based on his 26 years of clinical experience and the interview of 6 strong leaders for this book. Strategies that you can start using today to insure your child’s success.
Target Market(s)
parents and grandparents
Requirements
Must have
- a way to communicate strength in parenting

```html
<!DOCTYPE html>
<html lang="en">
<head>
<meta charset="utf-8">
<title>Never Stay Meek-Grow a Bold Captain — Book Cover</title>
<link href="https://fonts.googleapis.com/css2?family=Cinzel:wght@400;600;700&family=Questrial&display=swap" rel="stylesheet">
<style>
  :root {
    --navy: #0a2440;
    --ice: #e3f5fb;
    --ink: #111418;
    --subtitle-ink: #1f3a5a;
    --white: #ffffff;
    --band: rgba(120, 130, 140, 0.35);
  }
  html, body {
    margin: 0;
    padding: 0;
    width: 1200px;
    height: 960px;
    overflow: hidden;
    background: var(--white);
  }
  .canvas {
    position: relative;
    width: 1200px;
    height: 960px;
  }
  .back-cover, .spine, .front-cover { position: absolute; top: 110px; height: 740px; }

  /* Back cover */
  .back-cover { left: 50px; width: 500px; background: var(--navy); }
  .back-top {
    position: absolute; left: 0; top: 0; width: 500px; height: 370px;
    background: var(--ice);
  }
  .back-title {
    position: absolute; left: 0; top: 22px; width: 500px; margin: 0;
    font-family: "Cinzel", serif; font-weight: 600;
    font-size: 32px; line-height: 34px; text-align: center;
    color: var(--navy);
  }
  .blurb {
    font-family: "Questrial", sans-serif;
    font-size: 13px; line-height: 16.6px;
    text-align: justify; margin: 0;
  }
  .blurb p { margin: 0; text-indent: 28px; }
  .blurb-top { position: absolute; left: 40px; top: 114px; width: 419px; color: var(--ink); }
  .author-photo {
    position: absolute; left: 40px; top: 387px; width: 125px; height: 161px;
    background: var(--white);
  }
  .blurb-side {
    position: absolute; left: 182px; top: 393px; width: 278px; height: 166px;
    overflow: hidden; color: var(--white);
  }
  .blurb-bottom { position: absolute; left: 42px; top: 568px; width: 417px; color: var(--white); }

  /* Spine */
  .spine { left: 550px; width: 100px; background: var(--navy); }
  .spine-title {
    position: absolute; right: 12px; top: 46px;
    writing-mode: vertical-rl; margin: 0;
    font-family: "Cinzel", serif; font-weight: 400;
    font-size: 31px; line-height: 36px; color: var(--white);
    white-space: nowrap;
  }
  .spine-author {
    position: absolute; right: 32px; top: 526px;
    writing-mode: vertical-rl; margin: 0;
    font-family: "Cinzel", serif; font-weight: 400;
    font-size: 26px; color: var(--white); white-space: nowrap;
  }

  /* Front cover */
  .front-cover { left: 650px; width: 500px; overflow: hidden; }
  .cover-photo { position: absolute; inset: 0; }
  .front-title {
    position: absolute; left: 0; top: 392px; width: 500px; margin: 0;
    font-family: "Cinzel", serif; font-weight: 400;
    font-size: 46px; line-height: 50px; text-align: center;
    color: var(--ink);
  }
  .subtitle-band {
    position: absolute; left: 24px; top: 544px; width: 449px; height: 53px;
    background: var(--band);
  }
  .subtitle {
    position: absolute; left: 24px; top: 548px; width: 449px; margin: 0;
    font-family: "Cinzel", serif; font-weight: 400;
    font-size: 17px; line-height: 21px; text-align: center;
    color: var(--subtitle-ink);
  }
  .front-author {
    position: absolute; left: 0; top: 650px; width: 500px; margin: 0;
    font-family: "Cinzel", serif; font-weight: 700;
    font-size: 31px; text-align: center; color: var(--ink);
  }
</style>
</head>
<body>
<main class="canvas">

  <section class="back-cover">
    <div class="back-top"></div>
    <h2 class="back-title">Never Stay Meek-Grow<br>a Bold Captain</h2>
    <div class="blurb blurb-top">
      <p>What does it take to raise a strong leader? Psychologist Dr. Walter P. Ondrak provides you with 6 must do strategies based on his 26 years of clinical experience and the interview of 6 strong leaders for this book. Strategies that you can start using today to insure your child’s success.</p>
      <p>What does it take to raise a strong leader? Psychologist Dr. Walter P. Ondrak provides you with 6 must do strategies based on his 26 years of clinical experience and the interview of 6 strong leaders for this book. Strategies that you can start using today to insure your child’s success.</p>
      <p>What does it take to raise a strong leader? Psychologist Dr. Walter P. Ondrak provides you with 6 must do strategies based on his 26 years of clinical experience and the interview of 6 strong leaders for this book. Strategies that you can start using today to insure your child’s success.</p>
    </div>
    <div class="author-photo" role="img" aria-label="Author portrait placeholder"></div>
    <div class="blurb blurb-side">
      <p>What does it take to raise a strong leader? Psychologist Dr. Walter P. Ondrak provides you with 6 must do strategies based on his 26 years of clinical experience and the interview of 6 strong leaders for this book. Strategies that you can start using today to insure your child’s success.</p>
      <p>What does it take to raise a strong leader? Psychologist Dr. Walter P. Ondrak provides you with 6 must do strategies.</p>
    </div>
    <div class="blurb blurb-bottom">
      <p>What does it take to raise a strong leader? Psychologist Dr. Walter P. Ondrak provides you with 6 must do strategies based on his 26 years of clinical experience and the interview of 6 strong leaders for this book. Strategies that you can start using today to insure your child’s success.</p>
    </div>
  </section>

  <section class="spine">
    <h2 class="spine-title">Never Stay Meek-Grow<br>a Bold Captain</h2>
    <p class="spine-author">Dr. Walter</p>
  </section>

  <section class="front-cover">
    <svg class="cover-photo" width="500" height="740" role="img" aria-label="Photo of a smiling father in a white shirt while his young son helps knot his red tie, in a bright room">
      <defs>
        <linearGradient id="room-light" x1="0" y1="0" x2="1" y2="1">
          <stop offset="0" stop-color="#dcebf4"/>
          <stop offset="0.55" stop-color="#eef5f9"/>
          <stop offset="1" stop-color="#f7fafc"/>
        </linearGradient>
        <linearGradient id="fade-bottom" x1="0" y1="0" x2="0" y2="1">
          <stop offset="0.6" stop-color="#ffffff" stop-opacity="0"/>
          <stop offset="1" stop-color="#ffffff" stop-opacity="0.85"/>
        </linearGradient>
      </defs>
      <rect width="500" height="740" fill="url(#room-light)"/>
      <rect width="500" height="740" fill="url(#fade-bottom)"/>
    </svg>
    <h1 class="front-title">Never Stay<br>Meek-Grow<br>a Bold Captain</h1>
    <div class="subtitle-band"></div>
    <p class="subtitle">Family methods<br>from Cradle to Silver Years</p>
    <p class="front-author">by Dr. Walter P. Ondrak</p>
  </section>

</main>
</body>
</html>
```